Lender's Roundup - Edison NJ 2010

We need an event program designed for our Lender's Roundup events. We will have ten events in 2010 so we need a boiler plate layout for them all, however the thing that will change for each city are the speakers pictures, bios, logos and our ad sponsors. The program will include a cover page and on the backside of the cover page a Welcome page with a message from our founder. The next page (facing the inside front cover page) will be About the Lender's Roundup message. The next few pages will be reserved for our featured speakers and they will each have their own page to include their picture, company logo and bio. the remaining pages will be for our sponsors, which will vary by city/location. The back page should include the logos of all our sponsors, by category. I would like the brochure to be small in size...roughly 6 5/8" by 6 7/8". These are CEO events so the program needs to be professional, sophisticated, with an edge. Look at our website for more information about our next event on July 21st. I've included one of our speakers pictures, bio and company logo for setup purposes.

Target Market(s)

The attendees of our events are CEOs and Chief Decision Makers.

Industry/Entity Type

Events

Requirements
Must have
• The program must use all the photos, bios and logos we've attached.
Nice to have
• I like modern, clean lines, with a slight edge.
Should not have
• This should not be a consumer designed piece. It needs to have the WOW factor of professionalism.

```html
<!DOCTYPE html>
<html lang="en">
<head>
<meta charset="utf-8">
<title>A Note From Marisol Whitcombe – Lender's Roundup</title>
<link href="https://fonts.googleapis.com/css2?family=Arimo:ital@0;1&family=Roboto+Slab:wght@300&family=Noto+Serif:wght@700&display=swap" rel="stylesheet">
<style>
  :root {
    --accent-red: #cc0000;
    --ink: #000000;
    --paper: #ffffff;
  }
  html, body {
    margin: 0;
    padding: 0;
    overflow: hidden;
    background: var(--paper);
  }
  .page {
    position: relative;
    width: 1155px;
    height: 1200px;
    overflow: hidden;
    background: var(--paper);
    color: var(--ink);
    font-family: "Arimo", Arial, sans-serif;
  }
  .pull-quote-graphic {
    position: absolute;
    left: 0;
    top: 0;
    width: 1155px;
    height: 1200px;
  }
  .dotted-path {
    fill: none;
    stroke: var(--accent-red);
    stroke-width: 3;
    stroke-linecap: round;
    stroke-dasharray: 0 7;
  }
  .quote-glyph {
    fill: var(--accent-red);
    font-family: "Noto Serif", Georgia, serif;
    font-weight: 700;
  }
  .pull-quote-text {
    position: absolute;
    left: 762px;
    top: 136px;
    width: 320px;
    margin: 0;
    font-style: italic;
    font-size: 34px;
    line-height: 44px;
  }
  .note-heading {
    position: absolute;
    left: 96px;
    top: 1126px;
    transform: rotate(-90deg);
    transform-origin: 0 0;
    margin: 0;
    font-family: "Roboto Slab", Rockwell, serif;
    font-weight: 300;
    white-space: nowrap;
    line-height: 1;
  }
  .note-heading .note-label {
    display: block;
    font-size: 41px;
    margin-bottom: 4px;
  }
  .note-heading .note-author {
    display: block;
    font-size: 56px;
  }
  .dotted-rule {
    position: absolute;
    left: 211px;
    top: 570px;
    width: 12px;
    height: 560px;
  }
  .body-column {
    position: absolute;
    top: 567px;
    width: 338px;
    font-size: 20.8px;
    line-height: 26.6px;
  }
  .body-column p {
    margin: 0 0 26.6px;
  }
  .column-one { left: 242px; }
  .column-two { left: 589px; }
  .drop-cap {
    float: left;
    font-size: 58px;
    line-height: 48px;
    margin: 2px 2px 0 0;
  }
</style>
</head>
<body>
<main class="page">
  <svg class="pull-quote-graphic" viewBox="0 0 1155 1200" aria-hidden="true">
    <path class="dotted-path" d="M598 84 Q612 40 634 0"/>
    <circle class="dotted-path" cx="568" cy="200" r="120"/>
    <path class="dotted-path" d="M624 312 Q720 470 979 510"/>
    <circle class="dotted-path" cx="1043" cy="505" r="64"/>
    <path class="dotted-path" d="M1106 474 Q1130 458 1155 445"/>
    <text class="quote-glyph" x="568" y="348" font-size="270" text-anchor="middle">&#8220;</text>
    <text class="quote-glyph" x="1043" y="610" font-size="160" text-anchor="middle">&#8221;</text>
  </svg>

  <p class="pull-quote-text">A specific section of highlighted information can go here as a quote from the main body copy...</p>

  <h1 class="note-heading">
    <span class="note-label">A Note From</span>
    <span class="note-author">Marisol Whitcombe</span>
  </h1>

  <svg class="dotted-rule" viewBox="0 0 12 560" aria-hidden="true">
    <line x1="6" y1="3" x2="6" y2="557" stroke="#cc0000" stroke-width="5" stroke-linecap="round" stroke-dasharray="0 9"/>
  </svg>

  <div class="body-column column-one">
    <p><span class="drop-cap">L</span>orem ipsum dolor sit amet, consectetur adipiscing elit. In sem ligula, commodo a tincidunt in, placerat a nunc. Nunc tellus odio, rutrum suscipit dictum id, hendrerit et est. Aenean euismod vehicula lorem faucibus congue. Curabitur tempus leo vitae nisi iaculis eu accumsan nunc auctor. Aenean ut eros vitae tellus viverra tristique ultrices a lorem. Praesent sit amet nibh neque, vitae placerat lorem. Praesent lobortis ipsum quis eros congue ac viverra justo cursus. Proin ac lacus lacus. Fusce nisl magna, ultrices eu interdum eu, sagittis ac ligula. Suspendisse potenti. Nulla eros risus,</p>
  </div>

  <div class="body-column column-two">
    <p>suscipit eget vestibulum vitae, varius ac felis. Duis quam elit, porttitor et eleifend at, molestie eget ipsum. Nunc eget lectus lorem. Morbi enim metus, ullamcorper ac tempor ut, pretium a sapien. Donec ultrices felis augue.</p>
    <p>Aliquam fermentum tincidunt dui, molestie feugiat ligula dictum molestie. Donec ac arcu at lectus iaculis cursus nec sit amet nisl. Praesent accumsan nulla in sem consectetur non blandit libero sagittis. Curabitur vestibulum magna sit amet enim rhoncus vitae dapibus felis accumsan. Pellentesque felis augue,</p>
  </div>
</main>
</body>
</html>
```